Kestrel Bridge Consulting (KBC) Business Card Design

I would like to create double-sided business cards that contain:
1) Name: Derek Molvane
2) Phone Number: +1 (555) 218-4907
3) Email: Derek.Molvane@KestrelBridgeConsulting.example
4) Website: KestrelBridgeConsulting.example

I would like to include my logo and a color scheme similar to the Varnholt Grand Prix Ostera squad color scheme (black, silver, greenish-blue – but can also include regular blue)

What we do: Our company develops and delivers innovative and pragmatic information technology and cybersecurity risk and compliance solutions for organizations in the commercial market as well as the federal, and state/local sectors.

```html
<!DOCTYPE html>
<html lang="en">
<head>
<meta charset="utf-8">
<title>Kestrel Bridge Consulting – Business Card</title>
<link rel="stylesheet" href="https://fonts.googleapis.com/css2?family=Michroma&family=Roboto+Condensed:wght@400&display=swap">
<style>
  :root {
    --stage: #1b1b1c;
    --card-deep: #050d24;
    --card-mid: #0c1f45;
    --card-glow: #123c72;
    --ink-white: #f2f6fb;
    --brand-cyan: #12d6f5;
    --brand-blue: #1a7cf0;
    --teal-line: #1fa59a;
  }
  * { margin: 0; padding: 0; box-sizing: border-box; }
  html, body { width: 1200px; height: 1015px; overflow: hidden; background: var(--stage); }
  .canvas { position: relative; width: 1200px; height: 1015px; }

  .card {
    position: absolute;
    width: 640px; height: 366px;
    border-radius: 3px;
    overflow: hidden;
    box-shadow: 0 18px 40px rgba(0,0,0,.55);
  }
  .card-front { left: 110px; top: 90px;
    background: linear-gradient(160deg, var(--card-mid) 0%, var(--card-deep) 70%); }
  .card-back { left: 450px; top: 550px;
    background: linear-gradient(200deg, var(--card-mid) 0%, var(--card-deep) 75%); }

  .network-field {
    position: absolute; inset: 0;
    background: radial-gradient(ellipse at 78% 30%, rgba(26,90,160,.45) 0%, rgba(18,60,114,.18) 40%, transparent 70%);
  }
  .card-back .network-field {
    background: radial-gradient(ellipse at 80% 40%, rgba(18,214,245,.22) 0%, rgba(26,124,240,.14) 35%, transparent 68%);
  }

  .lockup {
    position: absolute; left: 150px; top: 128px;
    display: flex; align-items: center; gap: 22px;
  }
  .lockup-dot {
    width: 64px; height: 64px; border-radius: 50%;
    background: linear-gradient(150deg, var(--brand-cyan), var(--brand-blue));
  }
  .lockup-divider { width: 1px; height: 104px; background: var(--ink-white); opacity: .85; }
  .company-name {
    font-family: "Michroma", sans-serif;
    color: var(--ink-white);
    font-size: 25px; line-height: 32px;
    text-transform: uppercase; letter-spacing: 1px;
  }

  .contact-block { position: absolute; left: 44px; bottom: 40px; }
  .person-name {
    font-family: "Michroma", sans-serif;
    font-size: 26px; letter-spacing: 2px;
    text-transform: uppercase;
    background: linear-gradient(90deg, var(--brand-blue), var(--brand-cyan));
    -webkit-background-clip: text; background-clip: text; color: transparent;
  }
  .name-rule { width: 88px; height: 1px; background: var(--teal-line); margin: 12px 0 14px; }
  .contact-list { list-style: none; }
  .contact-item {
    display: flex; align-items: center; gap: 12px;
    font-family: "Roboto Condensed", sans-serif;
    color: var(--ink-white); font-size: 19px; line-height: 32px;
  }
  .contact-icon {
    width: 24px; height: 24px; flex: none;
  }
</style>
</head>
<body>
<main class="canvas">

  <section class="card card-front" aria-label="Card front">
    <div class="network-field" role="img" aria-label="Faint hexagonal network pattern in deep blue"></div>
    <div class="lockup">
      <span class="lockup-dot"></span>
      <span class="lockup-divider"></span>
      <h1 class="company-name">Kestrel<br>Bridge<br>Consulting</h1>
    </div>
  </section>

  <section class="card card-back" aria-label="Card back">
    <div class="network-field" role="img" aria-label="Hexagonal network pattern with soft cyan glow"></div>
    <div class="contact-block">
      <h2 class="person-name">Derek Molvane</h2>
      <div class="name-rule"></div>
      <ul class="contact-list">
        <li class="contact-item">
          <svg class="contact-icon" viewBox="0 0 24 24" aria-hidden="true">
            <circle cx="12" cy="12" r="11" fill="none" stroke="var(--teal-line)" stroke-width="1.3"/>
            <path d="M8.5 7.5c.6-.6 1.3-.5 1.7.1l.9 1.4c.3.5.2 1-.2 1.4l-.6.5c.5 1.2 1.5 2.2 2.7 2.7l.5-.6c.4-.4.9-.5 1.4-.2l1.4.9c.6.4.7 1.1.1 1.7l-.7.7c-2.6 1.1-8.1-4.4-7-7z" fill="var(--brand-cyan)"/>
          </svg>
          <span>+1 (555) 218-4907</span>
        </li>
        <li class="contact-item">
          <svg class="contact-icon" viewBox="0 0 24 24" aria-hidden="true">
            <circle cx="12" cy="12" r="11" fill="none" stroke="var(--teal-line)" stroke-width="1.3"/>
            <rect x="6.5" y="8" width="11" height="8" fill="var(--brand-cyan)"/>
            <path d="M6.5 8l5.5 4.5L17.5 8" fill="none" stroke="var(--card-deep)" stroke-width="1"/>
          </svg>
          <span>Derek.Molvane@KestrelBridgeConsulting.example</span>
        </li>
        <li class="contact-item">
          <svg class="contact-icon" viewBox="0 0 24 24" aria-hidden="true">
            <circle cx="12" cy="12" r="11" fill="none" stroke="var(--teal-line)" stroke-width="1.3"/>
            <g fill="none" stroke="var(--brand-cyan)" stroke-width="1">
              <circle cx="12" cy="12" r="5.5"/>
              <ellipse cx="12" cy="12" rx="2.4" ry="5.5"/>
              <path d="M6.5 12h11M7.3 9.3h9.4M7.3 14.7h9.4"/>
            </g>
          </svg>
          <span>KestrelBridgeConsulting.example</span>
        </li>
      </ul>
    </div>
  </section>

</main>
</body>
</html>
```